New Website - vostimo.net

This is what we looking for - http://www.craftlane-example.com/design/583017
Updates

hello, im back and i want some good designs for my website.. i need really creative ideas. this is for a cellphone provider company. Vostimo mobile please provide me a good ideas and i will go with u also to program the website

Font styles to use
Sans Serif

```html
<!DOCTYPE html>
<html lang="en">
<head>
<meta charset="utf-8">
<title>Vostimo Communications</title>
<link href="https://fonts.googleapis.com/css2?family=Open+Sans:wght@400;600&family=Ubuntu:wght@400;500&display=swap" rel="stylesheet">
<style>
:root{
  --header-bg:#4d4340;
  --blue:#0e9ad8;
  --blue-text:#3aa4e4;
  --btn-blue:#2b8fd6;
  --orange:#f0a21a;
  --orange-dark:#d98a0a;
  --text:#3c3c3c;
  --muted:#8a8a8a;
  --band:#f3f3f3;
  --line:#dcdcdc;
  --foot-top:#52c7ee;
  --foot-bottom:#1ea3dd;
}
*{margin:0;padding:0;box-sizing:border-box}
html,body{width:934px;height:1200px;overflow:hidden}
body{position:relative;background:#fff;font-family:"Open Sans",Arial,sans-serif;color:var(--text)}
.abs{position:absolute}
a{color:inherit;text-decoration:none}

/* header */
.site-header{left:0;top:0;width:934px;height:58px;background:var(--header-bg)}
.brand{left:146px;top:12px;display:flex;align-items:center;gap:7px;color:#fff}
.brand-dot{width:24px;height:24px;border-radius:50%;background:#6fb6e6}
.brand-name{font-family:"Ubuntu",sans-serif;font-size:26px;font-weight:400;line-height:1}
.brand-sub{left:190px;top:37px;color:#fff;font-size:7.5px;letter-spacing:2.6px}
.call{left:493px;top:21px;color:#fff;font-size:10px;display:flex;align-items:center;gap:5px}
.call-icon{width:15px;height:15px;border-radius:50%;background:#3d9ee0;display:flex;align-items:center;justify-content:center}
.call-num{font-size:11px}
.login{left:640px;top:21px;color:#fff;font-size:10px;display:flex;align-items:center;gap:4px}
.sep{top:24px;width:1px;height:8px;background:#7b716d}
.register{left:703px;top:16px;width:77px;height:23px;background:var(--btn-blue);color:#fff;font-size:9.5px;font-weight:600;display:flex;align-items:center;justify-content:center;gap:4px;border-radius:2px}

/* navigation */
.nav-bar{left:0;top:58px;width:934px;height:29px;border-bottom:1px solid var(--line);background:#fff}
.nav{left:145px;top:58px;height:29px;display:flex;font-size:11px}
.nav a{display:flex;align-items:center;justify-content:center;border-left:1px solid var(--line);color:#444}
.nav a.active{background:var(--orange);color:#fff;border-color:var(--orange)}
.nav a.account{border-right:none;justify-content:flex-start;padding-left:10px}
.caret{color:var(--btn-blue);font-size:7px;margin-left:3px}
.search{left:626px;top:64px;width:154px;height:17px;border:1px solid var(--line);font-size:8px;color:#999;padding-left:6px;display:flex;align-items:center}
.search svg{position:absolute;right:5px;top:2px}

/* hero */
.hero{left:145px;top:110px;width:635px;height:250px;border:1px solid #d8d8d8;background:#fff;overflow:hidden}
.hero-shadow{left:225px;top:360px;width:475px;height:30px;background:radial-gradient(ellipse at 50% 0,rgba(0,0,0,.14),rgba(0,0,0,0) 70%)}
.hero-photo{left:320px;top:10px;width:300px;height:230px;border-radius:40px;background:radial-gradient(ellipse at 55% 55%,#5a5f66 0,#3b3f45 45%,rgba(255,255,255,0) 72%)}
.hero-title{left:21px;top:30px;color:#fff;font-family:"Ubuntu",sans-serif;font-size:21px;line-height:24px}
.hero-sub{left:25px;top:86px;color:#fff;font-family:"Ubuntu",sans-serif;font-size:14.5px;line-height:20px}
.btn-orange{background:var(--orange);color:#fff;border-bottom:2px solid var(--orange-dark);display:flex;align-items:center;justify-content:center;font-family:"Ubuntu",sans-serif}
.hero-btn{left:46px;top:166px;width:95px;height:27px;font-size:12.5px}

/* intro */
.intro-title{left:144px;top:419px;color:var(--blue-text);font-family:"Ubuntu",sans-serif;font-size:21px;font-weight:500}
.intro-text{left:144px;top:450px;width:362px;color:var(--muted);font-size:10.3px;line-height:15.3px}
.intro-text p+p{margin-top:7px}
.intro-btn{left:144px;top:571px;width:83px;height:27px;font-size:12.5px}
.video{left:527px;top:428px;width:253px;height:159px;background:#fff;box-shadow:0 0 4px rgba(0,0,0,.25)}
.video-still{left:3px;top:3px;width:247px;height:142px;background:linear-gradient(100deg,#4a4a4c 0,#8c8f93 35%,#d8d4d0 60%,#b49a88 100%)}
.video-play{left:104px;top:46px;width:48px;height:48px;border-radius:8px;background:rgba(255,255,255,.85)}
.video-bar{left:3px;top:145px;width:247px;height:11px;background:#1b1b1b}

/* features */
.band{left:0;top:641px;width:934px;height:441px;background:var(--band)}
.col-title{font-family:"Ubuntu",sans-serif;font-size:19.5px;font-weight:500;color:var(--blue-text);text-align:center}
.col-sub{font-size:10px;text-align:center;color:#333}
.circle{border-radius:50%}
.bullets{list-style:none;font-size:9.6px;color:#555}
.bullets li{position:relative;padding-left:14px;height:20.8px}
.bullets li::before{content:"";position:absolute;left:0;top:5px;width:9px;height:4px;border-radius:50% 50% 50% 50%/100% 100% 0 0;background:var(--blue);transform:rotate(-20deg)}
.btn-pill{height:18px;border-radius:9px;background:var(--btn-blue);color:#fff;font-family:"Ubuntu",sans-serif;font-size:11.5px;display:flex;align-items:center;justify-content:center}
.flex-panel{left:594px;top:675px;width:187px;height:371px;background:var(--blue)}
.flex-panel .col-title,.flex-panel .col-sub{color:#fff}
.flex-panel .bullets{color:#fff}
.flex-panel .bullets li::before{background:#fff}
.keep{left:15px;top:232px;color:#fff;font-size:10.5px;font-weight:600;padding-left:14px;position:absolute}
.keep::before{content:"";position:absolute;left:0;top:5px;width:9px;height:4px;border-radius:50% 50% 50% 50%/100% 100% 0 0;background:#fff;transform:rotate(-20deg)}
.num-box{top:256px;width:21px;height:13px;background:#fff}
.check{left:110px;top:255px;width:59px;height:16px;font-size:9.5px;border:none;font-family:"Open Sans",sans-serif}

/* footer */
.site-footer{left:0;top:1082px;width:934px;height:118px;background:linear-gradient(var(--foot-top),var(--foot-bottom));border-top:2px solid #9bdcf3}
.social{left:428px;top:1101px;display:flex;gap:4px}
.social span{width:16px;height:16px;border-radius:50%;background:#fff}
.social span.alt{background:var(--orange)}
.foot-links{left:0;top:1128px;width:934px;text-align:center;color:#fff;font-size:10px}
.foot-links i{font-style:normal;margin:0 5px}
.foot-rule{left:205px;top:1156px;width:524px;height:1px;background:rgba(255,255,255,.25)}
.copy{left:0;top:1164px;width:934px;text-align:center;color:#fff;font-size:9.5px}
</style>
</head>
<body>

<header class="site-header abs"></header>
<div class="brand abs"><span class="brand-dot"></span><span class="brand-name">Vostimo</span></div>
<div class="brand-sub abs">COMMUNICATIONS</div>
<div class="call abs">Call Now
  <span class="call-icon"><svg width="8" height="8" viewBox="0 0 10 10"><path d="M2 1l2 2-1 1.2c.6 1.2 1.4 2 2.6 2.6L6.8 6 9 8 7.8 9.3C4.6 9 1 5.4.7 2.2z" fill="#fff"/></svg></span>
  <span class="call-num">555-010-4477</span></div>
<span class="sep abs" style="left:625px"></span>
<div class="login abs"><svg width="8" height="9" viewBox="0 0 8 9"><circle cx="4" cy="2.3" r="2.1" fill="#fff"/><path d="M0 9c0-3 1.6-4.3 4-4.3S8 6 8 9z" fill="#fff"/></svg>Login</div>
<span class="sep abs" style="left:690px"></span>
<a class="register abs"><svg width="8" height="9" viewBox="0 0 8 9"><circle cx="4" cy="2.3" r="2.1" fill="#fff"/><path d="M0 9c0-3 1.6-4.3 4-4.3S8 6 8 9z" fill="#fff"/></svg>REGISTER</a>

<div class="nav-bar abs"></div>
<nav class="nav abs">
  <a style="width:41px">Home</a>
  <a class="active" style="width:50px">Office</a>
  <a style="width:61px">Cellphone</a>
  <a style="width:56px">Support</a>
  <a style="width:50px">Contact</a>
  <a class="account" style="width:90px">My Account<span class="caret">&#9660;</span></a>
</nav>
<div class="search abs">Search Site
  <svg width="13" height="13" viewBox="0 0 13 13"><circle cx="8" cy="5" r="3.6" fill="none" stroke="#555" stroke-width="1.5"/><path d="M5.4 7.6L1.5 11.5" stroke="#555" stroke-width="2"/></svg></div>

<section class="hero abs">
  <div class="hero-photo abs" role="img" aria-label="Desk IP phone with handset and keypad"></div>
  <svg class="abs" style="left:0;top:0" width="635" height="250" viewBox="0 0 635 250">
    <path d="M7 8H356C290 40 240 110 222 243H215C228 120 272 40 338 8Z" fill="#bfe6f6"/>
    <path d="M7 8H338C272 40 228 120 215 243H7Z" fill="#0e9ad8"/>
  </svg>
  <h1 class="hero-title abs">A Revofutionary digital<br>Phone Service</h1>
  <p class="hero-sub abs">That will Save you,your family,<br>and your business lots<br>of money.</p>
  <a class="hero-btn btn-orange abs">View More</a>
</section>
<div class="hero-shadow abs"></div>

<h2 class="intro-title abs">Torem Ipsum as their default model</h2>
<div class="intro-text abs">
  <p>There are many variations of passages of Lorem Ipsum available, but the majority have suffered alteration in some form, by injected humour, or</p>
  <p>a passage of Lorem Ipsum, you need to be sure there isn't anything embar rassing hidden in the middle of text. All the Lorem Ipsum generators on the Internet tend to repeat predefined chunks as necessary, making this the first true generator on the Internet.It uses a dictionary of over 200 Latin words, combined with a handful of model..</p>
</div>
<a class="intro-btn btn-orange abs">View More</a>

<div class="video abs">
  <div class="video-still abs" role="img" aria-label="Office worker on the phone at a desk with a computer"></div>
  <div class="video-play abs"><svg width="48" height="48" viewBox="0 0 48 48"><path d="M19 14L34 24 19 34Z" fill="#1d2a3a"/></svg></div>
  <div class="video-bar abs"><svg width="247" height="11" viewBox="0 0 247 11"><path d="M5 3l4 2.5L5 8z" fill="#ccc"/><rect x="14" y="3" width="4" height="5" fill="#ccc"/><rect x="34" y="4.5" width="120" height="2" fill="#777"/><circle cx="36" cy="5.5" r="2" fill="#eee"/><rect x="200" y="3" width="5" height="5" fill="#c33"/><rect x="215" y="3" width="5" height="5" fill="#ccc"/><path d="M233 9h11V2z" fill="#888"/></svg></div>
</div>

<div class="band abs"></div>

<section class="abs" style="left:144px;top:686px;width:175px">
  <h3 class="col-title">Affordable</h3>
  <p class="col-sub">Start Saving Today!</p>
  <div class="circle abs" style="left:0;top:50px;width:173px;height:173px;background:radial-gradient(circle at 55% 62%,#f4c400 0,#e8b400 30%,#dfe4e8 55%,#f1f3f5 100%)" role="img" aria-label="Hand dropping a coin into a smiling yellow coin bank"></div>
  <ul class="bullets abs" style="left:0;top:230px;width:200px">
    <li>Unlimited local and long distance calling</li>
    <li>5 nation unlimited interntional</li>
    <li>No set-up, equipment fees, or hidden..</li>
    <li>No contracts or commitments</li>
  </ul>
  <a class="btn-pill abs" style="left:15px;top:320px;width:143px">View More</a>
</section>

<section class="abs" style="left:372px;top:686px;width:175px">
  <h3 class="col-title">Powerful</h3>
  <p class="col-sub">Incredible Features, Standard</p>
  <div class="circle abs" style="left:1px;top:50px;width:173px;height:173px;background:radial-gradient(circle at 45% 55%,#4a4c58 0,#22242c 55%,#3a3f5a 100%)" role="img" aria-label="Presenter on stage with a video play button"></div>
  <svg class="abs" style="left:74px;top:122px" width="30" height="30" viewBox="0 0 30 30"><rect width="30" height="30" rx="5" fill="rgba(255,255,255,.85)"/><path d="M11 8l10 7-10 7z" fill="#222"/></svg>
  <ul class="bullets abs" style="left:1px;top:230px;width:200px">
    <li>Seamless integration with Mailbox</li>
    <li>Get calls and voicemail anywhere</li>
    <li>100% hurricane proof</li>
    <li style="color:var(--blue-text);height:auto">Featuring the power of Linkstream!<br><span style="color:var(--orange);font-size:7.5px">See Vostimo in action!</span></li>
  </ul>
  <a class="btn-pill abs" style="left:26px;top:320px;width:143px">View More</a>
</section>

<section class="flex-panel abs">
  <h3 class="col-title" style="margin-top:11px">Flexible</h3>
  <p class="col-sub">Service on your own Terms</p>
  <div class="circle abs" style="left:16px;top:61px;width:161px;height:161px;background:radial-gradient(circle at 60% 50%,#c4544a 0,#6a2a2a 30%,#9aa2b0 55%,#e8ecf2 100%)" role="img" aria-label="Curved smartphone showing a clock screen"></div>
  <div class="keep">KEEP YOUR NUMBER!</div>
  <span class="num-box abs" style="left:27px"></span>
  <span class="num-box abs" style="left:55px"></span>
  <span class="num-box abs" style="left:82px"></span>
  <a class="check btn-orange abs">Check here</a>
  <ul class="bullets abs" style="left:15px;top:280px;width:165px">
    <li style="height:16px">Choose your own area code</li>
    <li style="line-height:13px">Custom-tailored business solutio ns, both hosted and local</li>
  </ul>
  <a class="btn-pill abs" style="left:19px;top:331px;width:143px;background:#fff;color:var(--orange)">View More</a>
</section>

<footer class="site-footer abs"></footer>
<div class="social abs"><span></span><span class="alt"></span><span></span><span></span></div>
<div class="foot-links abs">Home<i>|</i>Office<i>|</i>Cellphone<i>|</i>Support<i>|</i>Contact<i>|</i>My Account</div>
<div class="foot-rule abs"></div>
<div class="copy abs">&copy; 2014 vostimo.net</div>

</body>
</html>
```